DOUBLE SIDED BROCHURE NEEDED TO PROMOTE DOCTOR

I need a double sided DL size (99mm x 210mm) brochure, promoting a doctor seeing patients in a new area.

I want something professional. I have included the relevant information. I would also like the Dr's picture somwhere in the brochure, with a professional background. I wish to print these tomorrow, so i will pick a winner within 14 hours of posting this ad.

I have included an example of a brochures design that I recently saw, and its definietly a good starting point.

Medical

```html
<!DOCTYPE html>
<html lang="en">
<head>
<meta charset="utf-8">
<title>Surgeon Referral Flyer</title>
<link href="https://fonts.googleapis.com/css2?family=EB+Garamond:wght@400;600;700&display=swap" rel="stylesheet">
<style>
  :root {
    --orange: #e06b26;
    --charcoal: #4a4a4a;
    --paper: #f4f4f4;
    --blush: #e8dcdc;
    --ink: #1a1a1a;
    --soft-ink: #3c3c3c;
    --light-text: #e4e4e4;
    --white: #ffffff;
  }
  html, body { margin: 0; padding: 0; overflow: hidden; }
  body { width: 1200px; height: 1200px; background: var(--white); }
  .flyer {
    position: relative; width: 1200px; height: 1200px; overflow: hidden;
    font-family: "EB Garamond", Georgia, serif; color: var(--ink);
    background: linear-gradient(160deg, #f7f7f7 0%, var(--paper) 45%, #fafafa 100%);
  }
  .shapes { position: absolute; inset: 0; }
  .text { position: absolute; margin: 0; white-space: nowrap; }
  .greeting { left: 40px; top: 68px; font-size: 34px; }
  .intro { left: 40px; top: 122px; font-size: 34px; line-height: 44px; }
  .intro p { margin: 0 0 16px; }
  .specialty-heading { left: 22px; top: 644px; font-size: 23px; line-height: 32px; font-weight: 700; }
  .specialty-list { left: 20px; top: 738px; font-size: 24px; line-height: 34px; list-style: none; padding: 0; }
  .specialty-list li::before { content: "❖"; font-size: 18px; margin-right: 6px; color: var(--soft-ink); }
  .specialty-list .continued { padding-left: 25px; margin-top: -5px; }
  .specialty-list .continued::before { content: none; }
  .general-heading { left: 810px; top: 644px; font-size: 23px; line-height: 32px; font-weight: 600; color: var(--white); }
  .general-list { list-style: none; padding: 0; font-size: 24px; line-height: 30px; color: var(--light-text); }
  .general-list li { position: relative; padding-left: 30px; margin-bottom: 4px; }
  .general-list li::before { content: "❖"; position: absolute; left: 0; font-size: 18px; color: var(--orange); }
  .general-list .etc { padding-left: 30px; }
  .general-list .etc::before { content: none; }
  .col-one { left: 812px; top: 738px; }
  .col-two { left: 1026px; top: 738px; }
  .clinic { left: 38px; top: 918px; font-size: 28px; line-height: 36px; color: var(--ink); }
  .divider { position: absolute; left: 337px; top: 912px; width: 2px; height: 114px; background: var(--white); }
  .phone { left: 396px; top: 922px; font-size: 68px; font-weight: 700; color: var(--ink); letter-spacing: 0.5px; }
  .referral-note { left: 38px; top: 1080px; font-size: 27px; color: var(--soft-ink); }
  .fax { left: 38px; top: 1114px; font-size: 34px; font-weight: 700; color: var(--soft-ink); }
</style>
</head>
<body>
<div class="flyer">
  <svg class="shapes" width="1200" height="1200" viewBox="0 0 1200 1200" aria-hidden="false">
    <defs>
      <linearGradient id="photoTone" x1="0" y1="0" x2="0.6" y2="1">
        <stop offset="0" stop-color="#3f7fc9"/>
        <stop offset="0.4" stop-color="#a9c6e6"/>
        <stop offset="0.7" stop-color="#7a8790"/>
        <stop offset="1" stop-color="#2a3038"/>
      </linearGradient>
    </defs>
    <rect class="top-edge" x="0" y="0" width="1200" height="29" fill="var(--blush)"/>
    <polygon class="hero-photo" role="img" aria-label="Photo of the surgeon smiling in front of a modern hospital building under a blue sky"
      points="900,29 1200,29 1200,592 632,592" fill="url(#photoTone)"/>
    <rect class="gap-band" x="0" y="592" width="1200" height="20" fill="var(--white)"/>
    <polygon class="band-main" points="0,484 648,484 608,568 0,568" fill="var(--orange)"/>
    <polygon class="band-accent" points="684,484 840,484 800,568 644,568" fill="var(--orange)"/>
    <polygon class="band-stripe" points="850,484 874,484 834,568 810,568" fill="var(--orange)"/>
    <polygon class="band-white" points="880,484 1200,484 1200,568 856,568" fill="var(--white)"/>
    <polygon class="services-panel" points="796,612 1200,612 1200,888 664,888" fill="var(--charcoal)"/>
    <polygon class="contact-band" points="0,888 1092,888 1036,1050 0,1050" fill="var(--orange)"/>
    <polygon class="footer-panel" points="528,1176 584,1050 1036,1050 1092,888 1176,888 1124,1050 1200,1050 1200,1176" fill="var(--charcoal)"/>
    <polygon class="contact-stripe" points="1116,888 1148,888 1094,1050 1062,1050" fill="var(--orange)"/>
    <rect class="bottom-edge" x="0" y="1176" width="1200" height="24" fill="var(--blush)"/>
  </svg>

  <div class="text greeting">Dear Doctors,</div>
  <div class="text intro">
    <p>We are pleased to announce that Dr.KarimHaddad is<br>now consulting in Mandurah, seeing public and<br>private patients.</p>
    <p>Guaranteed appointment within two weeks, with<br>patients having the option of surgery at<br>Coastal Health Campus, Banksia Vale Hospital or<br>St. Elara Private Hospital.</p>
  </div>

  <div class="text specialty-heading">Dr.Haddad is a highly trained specialised surgeon, in all areas of<br>Endocrine, Breast and General Surgery. Including;</div>
  <ul class="text specialty-list">
    <li>Thyroid Surgery</li>
    <li>Parathyroid surgery (including minimally invasive parathyroidectomy)</li>
    <li>Breast Cancer</li>
    <li class="continued">Benign breast lesions</li>
  </ul>

  <div class="text general-heading">All areas of general surgery,<br>such as;</div>
  <ul class="text general-list col-one">
    <li>Gallbladder<br>surgery</li>
    <li>Hernia surgery</li>
  </ul>
  <ul class="text general-list col-two">
    <li>Haemorrhoids</li>
    <li>Carpal Tunnel</li>
    <li>Vasectomy</li>
    <li class="etc">etc etc…</li>
  </ul>

  <div class="text clinic">Mandurah Clinic:<br>42 Harbourview Road<br>Mandurah WA 6210.</div>
  <div class="divider"></div>
  <div class="text phone">Phone: 1300 482 716</div>

  <div class="text referral-note">Please send all referrals by fax to</div>
  <div class="text fax">(08) 6421 3058</div>
</div>
</body>
</html>
```